We want a business card/punch card for our business. We are including examples of our current business card (we like the front of our business card and not looking to remake it). We need only back side to be designed in form of a punch card (we are including a sample of the punch card we made, but are unsatisfied). For each $180 spend (9 punches) our clients have $20 off.

Colors
886aae

```html
<!DOCTYPE html>
<html lang="en">
<head>
<meta charset="utf-8">
<title>Lunar Flow Studio – Loyalty Card</title>
<link rel="stylesheet" href="https://fonts.googleapis.com/css2?family=Cormorant+Garamond:ital,wght@0,500;0,600;1,500&family=Open+Sans:wght@400&display=swap">
<style>
  :root {
    --page-bg: #ecebec;
    --card-bg: #060608;
    --periwinkle: #6a72cc;
    --brand-violet: #886aae;
    --teal-light: #3cc9c0;
    --teal-dark: #0d3f42;
    --white: #f4f4f6;
    --divider: #2a2c55;
  }
  * { box-sizing: border-box; margin: 0; padding: 0; }
  html, body { width: 1200px; height: 1200px; overflow: hidden; }
  body {
    background: var(--page-bg);
    position: relative;
    font-family: "Open Sans", sans-serif;
  }
  .card {
    position: absolute;
    left: 170px;
    width: 860px;
    height: 490px;
    background: var(--card-bg);
    border-radius: 34px;
    overflow: hidden;
  }
  .card--front { top: 70px; }
  .card--back { top: 640px; }

  /* Front */
  .front__artwork {
    position: absolute;
    left: 30px; top: 110px;
    width: 400px; height: 350px;
    border-radius: 12px;
    background: radial-gradient(ellipse at 35% 55%, var(--teal-light) 0%, #1a8c88 35%, var(--teal-dark) 70%, var(--card-bg) 100%);
  }
  .front__brand {
    position: absolute;
    right: 40px; top: 48px;
    width: 400px;
    text-align: center;
    font-family: "Cormorant Garamond", serif;
    font-weight: 600;
    font-size: 50px;
    line-height: 1;
    color: var(--periwinkle);
  }
  .front__message {
    position: absolute;
    right: 40px; top: 160px;
    width: 400px;
    text-align: center;
    font-size: 16px;
    line-height: 1.45;
    color: var(--periwinkle);
  }
  .front__message p + p { margin-top: 14px; }
  .front__url {
    position: absolute;
    right: 40px; bottom: 50px;
    width: 400px;
    text-align: center;
    font-family: "Cormorant Garamond", serif;
    font-style: italic;
    font-size: 26px;
    color: var(--periwinkle);
  }

  /* Back */
  .back__identity {
    position: absolute;
    left: 0; top: 0;
    width: 400px; height: 490px;
    display: flex; flex-direction: column;
    align-items: center; justify-content: center;
    gap: 26px;
  }
  .back__mark {
    width: 90px; height: 90px;
    border-radius: 50%;
    border: 3px solid var(--brand-violet);
  }
  .back__brand {
    font-family: "Cormorant Garamond", serif;
    font-weight: 600;
    font-size: 48px;
    line-height: 1;
    color: var(--periwinkle);
    text-align: center;
  }
  .back__divider {
    position: absolute;
    left: 400px; top: 70px;
    width: 1px; height: 350px;
    background: var(--divider);
  }
  .punch {
    position: absolute;
    left: 430px; top: 50px;
    width: 400px;
    text-align: center;
  }
  .punch__title {
    font-family: "Cormorant Garamond", serif;
    font-weight: 600;
    font-size: 38px;
    letter-spacing: 2px;
    color: var(--periwinkle);
    line-height: 1.1;
  }
  .punch__thanks {
    font-family: "Cormorant Garamond", serif;
    font-weight: 600;
    font-size: 17px;
    color: var(--white);
    margin-top: 2px;
  }
  .punch__grid {
    display: grid;
    grid-template-columns: repeat(4, 64px);
    gap: 18px 26px;
    justify-content: center;
    margin-top: 28px;
  }
  .punch__slot {
    width: 64px; height: 64px;
    border-radius: 50%;
    border: 2.5px solid var(--periwinkle);
    display: flex; align-items: center; justify-content: center;
    font-family: "Cormorant Garamond", serif;
    font-weight: 600;
    font-size: 32px;
    color: var(--periwinkle);
  }
  .punch__slot--nine { grid-column: 3; }
  .punch__slot--reward {
    grid-column: 4;
    background: var(--periwinkle);
    color: var(--card-bg);
    font-size: 22px;
  }
  .back__url {
    position: absolute;
    left: 430px; bottom: 40px;
    width: 400px;
    text-align: center;
    font-family: "Cormorant Garamond", serif;
    font-style: italic;
    font-weight: 500;
    font-size: 26px;
    color: var(--white);
  }
</style>
</head>
<body>
  <section class="card card--front">
    <div class="front__artwork" role="img" aria-label="Teal seated meditation statue beside a floating lotus flower reflected in water"></div>
    <div class="front__brand">Lunar Flow Studio</div>
    <div class="front__message">
      <p>This cards is a symbol of appreciation from us to you without your business we would not be able to what we love most.</p>
      <p>When you fillout this card you will receive $20 toward your next weekly Event workshop or Private Session</p>
    </div>
    <div class="front__url">www.lunarflowstudio.com</div>
  </section>

  <section class="card card--back">
    <div class="back__identity">
      <div class="back__mark"></div>
      <div class="back__brand">Lunar Flow<br>Studio</div>
    </div>
    <div class="back__divider"></div>
    <div class="punch">
      <h2 class="punch__title">YOGA STUDIO</h2>
      <p class="punch__thanks">Thank you for your loyalty</p>
      <div class="punch__grid">
        <span class="punch__slot">1</span>
        <span class="punch__slot">2</span>
        <span class="punch__slot">3</span>
        <span class="punch__slot">4</span>
        <span class="punch__slot">5</span>
        <span class="punch__slot">6</span>
        <span class="punch__slot">7</span>
        <span class="punch__slot">8</span>
        <span class="punch__slot punch__slot--nine">9</span>
        <span class="punch__slot punch__slot--reward">$20</span>
      </div>
    </div>
    <div class="back__url">www.lunarflowstudio.com</div>
  </section>
</body>
</html>
```